Wedding logo

a simple design to be used on letterhead/menus for wedding
" Lorena & Victor"
palm branch or similar - tropical foliage

Industry/Entity Type

Wedding

Font styles to use
Decorative
Script

Colors
9bcb3c

Requirements
Must have
• names
• green foliage
Nice to have
• similar font to picture sent
Should not have
• too much color

```html
<!DOCTYPE html>
<html lang="en">
<head>
<meta charset="utf-8">
<title>Lorena &amp; Victor – Letterhead</title>
<link rel="stylesheet" href="https://fonts.googleapis.com/css2?family=Great+Vibes&family=Questrial&family=Roboto+Slab:wght@500&display=swap">
<style>
  :root {
    --paper: #ffffff;
    --board: #ffffff;
    --leaf-light: #8dc63f;
    --leaf-dark: #2f6e1c;
    --leaf-mid: #4f9a2a;
    --label: #80b04a;
    --label-text: #ffffff;
    --body-text: #6b6b6b;
    --shadow: rgba(0, 0, 0, 0.28);
  }
  * { margin: 0; padding: 0; box-sizing: border-box; }
  html, body { width: 1200px; height: 1154px; overflow: hidden; background: var(--board); }
  .board { position: relative; width: 1200px; height: 1154px; }

  .sheet {
    position: absolute;
    width: 560px; height: 792px;
    background: var(--paper);
    box-shadow: 5px 6px 6px var(--shadow);
    overflow: hidden;
  }
  .sheet--blank { left: 30px; top: 25px; }
  .sheet--filled { left: 638px; top: 348px; }

  .foliage { position: absolute; }
  .foliage--top-left {
    left: 0; top: 0; width: 135px; height: 95px;
    border-radius: 0 0 70% 0;
    background: radial-gradient(circle at 30% 30%, var(--leaf-mid), var(--leaf-dark) 75%);
  }
  .foliage--top-right {
    right: 0; top: 0; width: 185px; height: 92px;
    border-radius: 0 0 0 80%;
    background: radial-gradient(circle at 70% 25%, var(--leaf-mid), var(--leaf-dark) 75%);
  }
  .foliage--bottom-left {
    left: 0; bottom: 0; width: 160px; height: 148px;
    border-radius: 0 80% 0 0;
    background: radial-gradient(circle at 30% 70%, var(--leaf-mid), var(--leaf-dark) 75%);
  }

  .masthead {
    position: absolute; left: 36px; top: 120px; width: 490px; height: 46px;
    display: flex; align-items: center; justify-content: space-between;
  }
  .masthead__ornament {
    width: 118px; height: 24px; border-radius: 12px;
    background: linear-gradient(90deg, rgba(79,154,42,0.15), rgba(79,154,42,0.5), rgba(79,154,42,0.15));
  }
  .couple-name {
    font-family: "Questrial", sans-serif;
    font-weight: 400;
    color: var(--leaf-mid);
    white-space: nowrap;
  }
  .couple-name--head { font-size: 26px; }
  .couple-name--foot { font-size: 18px; }

  .sign-off {
    position: absolute; left: 326px; top: 642px; width: 210px;
    display: flex; flex-direction: column; align-items: center; gap: 6px;
  }
  .sign-off__ornament {
    width: 200px; height: 10px; border-radius: 5px;
    background: linear-gradient(90deg, rgba(79,154,42,0.15), rgba(79,154,42,0.45), rgba(79,154,42,0.15));
  }

  .event-line {
    position: absolute; left: 198px; top: 732px;
    font-family: "Great Vibes", cursive; font-size: 17px; color: var(--leaf-mid);
  }

  .recipient { position: absolute; left: 40px; top: 178px; color: var(--leaf-dark); }
  .recipient__to, .recipient__name { font-family: "Great Vibes", cursive; font-size: 20px; line-height: 22px; }
  .recipient__contact {
    margin-top: 6px;
    font-family: "Questrial", sans-serif; font-size: 8px; line-height: 12px; color: var(--leaf-dark);
  }

  .letter-body {
    position: absolute; left: 41px; top: 298px; width: 465px;
    font-family: "Questrial", sans-serif; font-size: 8.4px; line-height: 10.5px; color: var(--body-text);
  }
  .letter-body p { margin-bottom: 11px; }

  .label { position: absolute; height: 70px; display: flex; align-items: center; }
  .label__text {
    background: var(--label); color: var(--label-text);
    font-family: "Roboto Slab", serif; font-weight: 500; font-size: 19px;
    height: 48px; line-height: 48px; padding: 0 14px; white-space: nowrap;
  }
  .label--blank { left: 612px; top: 154px; }
  .label--filled { left: 123px; top: 872px; }
  .label__text--blank { width: 245px; margin-left: 5px; }
  .label__text--filled { width: 400px; margin-right: 4px; }
</style>
</head>
<body>
<div class="board">

  <section class="sheet sheet--blank">
    <div class="foliage foliage--top-left" role="img" aria-label="Tropical palm leaves in the corner"></div>
    <div class="foliage foliage--top-right" role="img" aria-label="Monstera leaf with berry sprigs in the corner"></div>
    <div class="masthead">
      <div class="masthead__ornament" role="img" aria-label="Leafy scroll ornament"></div>
      <span class="couple-name couple-name--head">Lorena &amp; Victor</span>
      <div class="masthead__ornament" role="img" aria-label="Leafy scroll ornament"></div>
    </div>
    <div class="foliage foliage--bottom-left" role="img" aria-label="Monstera leaves with a white frangipani flower"></div>
    <div class="sign-off">
      <span class="couple-name couple-name--foot">Lorena &amp; Victor</span>
      <div class="sign-off__ornament" role="img" aria-label="Leafy divider ornament"></div>
    </div>
    <div class="event-line">Date, Event , Location info can go here...........</div>
  </section>

  <div class="label label--blank">
    <svg width="52" height="70" viewBox="0 0 52 70"><polygon points="0,35 28,0 28,11 52,11 52,59 28,59 28,70" fill="#80b04a"/></svg>
    <div class="label__text label__text--blank">BLANK LETTER HEAD</div>
  </div>

  <section class="sheet sheet--filled">
    <div class="foliage foliage--top-left" role="img" aria-label="Tropical palm leaves in the corner"></div>
    <div class="foliage foliage--top-right" role="img" aria-label="Monstera leaf with berry sprigs in the corner"></div>
    <div class="masthead">
      <div class="masthead__ornament" role="img" aria-label="Leafy scroll ornament"></div>
      <span class="couple-name couple-name--head">Lorena &amp; Victor</span>
      <div class="masthead__ornament" role="img" aria-label="Leafy scroll ornament"></div>
    </div>

    <div class="recipient">
      <div class="recipient__to">To</div>
      <div class="recipient__name">Nora Bellamy</div>
      <div class="recipient__contact">
        <div>Address: 42/7, Palm Grove Lane, Seabrook- 21</div>
        <div>Web: www.greenleafstudio.com, Email: info@greenleafstudio.com</div>
        <div>Ph: +91 90000 12345</div>
      </div>
    </div>

    <div class="letter-body">
      <p>Dear guest, we are delighted to share the plans for our wedding day with you. The ceremony will be held in the garden, followed by dinner under the palms and music until late. Please let us know about any dietary needs so the kitchen can prepare a fitting menu for every guest at the table.</p>
      <p>Guests arriving early may enjoy a welcome drink on the terrace. Shuttles leave the hotel every half hour from noon, and parking is available beside the main gate for those who drive. Light shade and seating will be set along the path.</p>
      <p>The dress code is garden formal, and soft colours suit the setting well. Comfortable shoes are a good idea, as the lawn leads down to the water. A photographer will be with us all afternoon. Please reply by the first of May so we can confirm the final numbers with the venue.</p>
      <p>We look forward to celebrating with you. Children are most welcome, and a quiet room is ready for naps.</p>
      <p>Gifts are not expected, though a small card box will stand by the entrance. Your presence means more to us than anything else.</p>
      <p>If you have any questions, write to us or call at any time. Rooms nearby are held under our names until the end of the month. With love and thanks for being part of our story. See you soon.</p>
    </div>

    <div class="foliage foliage--bottom-left" role="img" aria-label="Monstera leaves with a white frangipani flower"></div>
    <div class="sign-off">
      <span class="couple-name couple-name--foot">Lorena &amp; Victor</span>
      <div class="sign-off__ornament" role="img" aria-label="Leafy divider ornament"></div>
    </div>
    <div class="event-line">Date, Event , Location info can go here...........</div>
  </section>

  <div class="label label--filled">
    <div class="label__text label__text--filled">LETTER HEAD WITH DUMMY CONTENT</div>
    <svg width="52" height="70" viewBox="0 0 52 70"><polygon points="52,35 24,0 24,11 0,11 0,59 24,59 24,70" fill="#80b04a"/></svg>
  </div>

</div>
</body>
</html>
```